Logo design, letter head, cover page and business card

Provide a graphic package (stationary) for a construction Aluminum manufacturing company. Windows, doors, steel structure, beams, columns, etc.
The graphic package to include the following:
> Business Card
> Logo
> Letter head/footer
> Cover page

The company name is: Tevani Contracting & General Maintenance (TGM); you can use the acronym "TGM".

```html
<!DOCTYPE html>
<html lang="en">
<head>
<meta charset="utf-8">
<title>Tevani Contracting &amp; General Maintenance — Stationery</title>
<link href="https://fonts.googleapis.com/css2?family=Josefin+Sans:wght@300;400&family=Open+Sans:wght@400;600&display=swap" rel="stylesheet">
<style>
  :root {
    --canvas: #e9e9e7;
    --paper: #ffffff;
    --ink: #2b2b2b;
    --ink-soft: #555555;
    --line: #d6d6d6;
  }
  html, body {
    margin: 0;
    padding: 0;
    overflow: hidden;
  }
  .stationery {
    position: relative;
    width: 1200px;
    height: 797px;
    background: var(--canvas);
    overflow: hidden;
    font-family: "Open Sans", sans-serif;
    color: var(--ink);
  }
  .letterhead {
    position: absolute;
    left: 137px;
    top: 117px;
    width: 263px;
    height: 373px;
    background: var(--paper);
    box-shadow: 0 1px 3px rgba(0,0,0,0.12);
    box-sizing: border-box;
    padding: 38px 30px 0 58px;
  }
  .brand {
    display: flex;
    flex-direction: column;
    align-items: flex-start;
  }
  .brand-mark {
    width: 22px;
    height: 22px;
    border: 1px solid var(--ink);
    border-radius: 50%;
    margin: 0 0 6px 13px;
  }
  .brand-name {
    font-family: "Josefin Sans", sans-serif;
    font-weight: 300;
    font-size: 15px;
    letter-spacing: 1px;
    line-height: 1;
    color: var(--ink);
  }
  .brand-tagline {
    font-family: "Josefin Sans", sans-serif;
    font-weight: 300;
    font-size: 4.6px;
    letter-spacing: 0.2px;
    margin-top: 2px;
    color: var(--ink-soft);
  }
  .letter-salutation {
    font-size: 6.4px;
    font-weight: 600;
    margin: 32px 0 19px;
  }
  .letter-body p {
    font-size: 4.9px;
    line-height: 8.3px;
    margin: 0 0 8px;
    color: var(--ink-soft);
  }
  .card {
    position: absolute;
    left: 480px;
    width: 107px;
    height: 66px;
    background: var(--paper);
    box-shadow: 0 1px 3px rgba(0,0,0,0.14);
    box-sizing: border-box;
  }
  .card-front {
    top: 222px;
    display: flex;
    align-items: center;
    justify-content: center;
    gap: 5px;
  }
  .card-front .card-mark {
    width: 18px;
    height: 18px;
    border: 1px solid var(--ink);
    border-radius: 50%;
  }
  .card-front .card-monogram {
    font-family: "Josefin Sans", sans-serif;
    font-weight: 300;
    font-size: 9px;
    letter-spacing: 1px;
  }
  .card-back {
    top: 345px;
    padding: 21px 0 0 28px;
  }
  .card-back .brand-name {
    font-size: 9px;
    letter-spacing: 0.6px;
  }
  .card-back .brand-tagline {
    font-size: 3px;
    margin-top: 1px;
  }
  .card-contact {
    margin-top: 8px;
    padding-top: 3px;
    font-size: 3.2px;
    line-height: 5px;
    color: var(--ink-soft);
  }
</style>
</head>
<body>
<main class="stationery">

  <article class="letterhead">
    <header class="brand">
      <span class="brand-mark"></span>
      <span class="brand-name">TEVANI</span>
      <span class="brand-tagline">Contracting &amp; General Maintenance</span>
    </header>
    <p class="letter-salutation">Dear Mr. Harlow,</p>
    <div class="letter-body">
      <p>Lorem ipsum dolor sit amet, consectetur adipiscing elit. Donec orci purus, luctus vitae dignissim eu, iaculis sed purus. Vivamus faucibus, ipsum nec aliquet viverra, leo mauris condimentum ligula, sit amet sagittis enim ligula quis arcu. Nam egestas tortor id nisi porttitor mattis. In tortor ante, ultricies in suscipit a, tempus non massa. Vivamus et auctor mi. Fusce vel massa nulla.</p>
      <p>Donec malesuada orci vitae nulla accumsan porta a id massa. Quisque accumsan iaculis magna sit amet fringilla. Maecenas consequat, magna eget tincidunt semper, odio nibh rutrum mi, id feugiat ante nisi eu risus.</p>
      <p>Duis aute irure dolor in reprehenderit in voluptate velit esse cillum dolore eu fugiat nulla pariatur. Excepteur sint occaecat cupidatat non proident, sunt in culpa qui officia deserunt mollit anim id est laborum. Sed ut perspiciatis unde omnis iste natus error sit voluptatem accusantium doloremque laudantium.</p>
    </div>
  </article>

  <section class="card card-front" aria-label="Business card front">
    <span class="card-mark"></span>
    <span class="card-monogram">TGM</span>
  </section>

  <section class="card card-back" aria-label="Business card back">
    <div class="brand-name">TEVANI</div>
    <div class="brand-tagline">Contracting &amp; General Maintenance</div>
    <div class="card-contact">
      (512) 555-0187 &nbsp;|&nbsp; hello@tevanigm.com<br>
      48 Harbor Lane, Riverton, NY 10001, US
    </div>
  </section>

</main>
</body>
</html>
```